Business Card Design and stationary (thank you cards)

I am basically starting a "handyman" business but have a little ego issue with that term. I have been a professional in the design and construction business for 30 years. I want simple…I will define the scope of work I do as i move forward, and it can vary and i want it to vary.

Target Market(s)

Homeowners mostly

Industry/Entity Type

Business

Contact Information for Business Card

Company Name is "Tidy Corner Crew" Dale P. Whitcombe, 42 Larkvale Hollow Road, Wrenford, Ct, 06419 (but I may want to use a PO Box), Phone is 860-555-0187, email is dwhitcombe584@mailnest.example,

Font styles to use
Sans Serif

Requirements
Should not have
• anything pre designed….hammers or whatever…custom lines to make home features as shone but simple and elegant

```html
<!DOCTYPE html>
<html lang="en">
<head>
<meta charset="utf-8">
<title>Tidy Corner Crew – Business Card</title>
<link href="https://fonts.googleapis.com/css2?family=Arimo:wght@400;500&display=swap" rel="stylesheet">
<style>
  :root {
    --ink: #1f262d;
    --paper: #ffffff;
    --rust: #9b3426;
    --rule-soft: #5b6269;
    --text: #111111;
  }
  * { margin: 0; padding: 0; box-sizing: border-box; }
  html, body { width: 1200px; height: 351px; overflow: hidden; background: var(--paper); }
  body { font-family: "Arimo", Arial, sans-serif; }

  .card { position: relative; width: 1200px; height: 351px; background: var(--paper); overflow: hidden; }

  /* Header band */
  .header { position: absolute; left: 0; top: 0; width: 1200px; height: 95px; background: var(--ink); }
  .header-divider { position: absolute; left: 599px; top: 0; width: 1px; height: 95px; background: var(--rule-soft); }
  .header-rule { position: absolute; left: 0; top: 71px; width: 599px; height: 2px; background: var(--paper); }
  .header-rule--right { left: 600px; width: 600px; height: 1px; background: var(--rule-soft); }
  .brand-name {
    position: absolute; left: 150px; top: 45px;
    color: var(--paper); font-size: 26px; font-weight: 400; letter-spacing: 0.3px; line-height: 1;
    text-transform: uppercase;
  }

  /* Services */
  .services { list-style: none; }
  .service {
    position: absolute; width: 200px; margin-left: -100px; text-align: center;
    color: var(--rust); font-size: 20px; line-height: 1;
  }

  .tagline, .offer {
    position: absolute; width: 320px; margin-left: -160px; text-align: center;
    color: var(--text); font-size: 30px; line-height: 37px; text-transform: uppercase;
  }
  .tagline { left: 170px; top: 198px; }
  .offer { left: 479px; top: 198px; }
  .wobble { display: inline-block; }
  .wobble--up { transform: translateY(-4px) rotate(-4deg); }
  .wobble--down { transform: translateY(3px) rotate(5deg); }
  .wobble--tilt { transform: rotate(-8deg); }

  /* Address */
  .address-frame { position: absolute; left: 0; top: 0; }
  .address {
    position: absolute; left: 887px; top: 194px; width: 440px;
    transform: translate(-50%, -50%) rotate(-5deg);
    text-align: center; color: var(--text); font-size: 29px; line-height: 35px; font-style: normal;
  }

  /* Footer band */
  .footer { position: absolute; left: 0; top: 286px; width: 1200px; height: 65px; background: var(--ink); }
  .footer-cut { position: absolute; left: 0; top: 0; }
  .owner-name {
    position: absolute; left: 29px; top: 21px;
    color: var(--paper); font-size: 21px; line-height: 1; text-transform: uppercase;
  }
  .phone {
    position: absolute; left: 362px; top: 16px; display: flex; align-items: center; gap: 10px;
    color: var(--paper); font-size: 27px; line-height: 1;
  }
  .phone-icon { width: 26px; height: 28px; }
  .email {
    position: absolute; left: 906px; top: 17px; transform: translateX(-50%);
    color: var(--paper); font-size: 26px; line-height: 1; white-space: nowrap;
  }
</style>
</head>
<body>
<div class="card">

  <header class="header">
    <div class="header-rule"></div>
    <div class="header-rule header-rule--right"></div>
    <div class="header-divider"></div>
    <div class="brand-name">Tidy Corner Crew</div>
  </header>

  <ul class="services">
    <li class="service" style="left:101px; top:112px;">Electrical</li>
    <li class="service" style="left:293px; top:112px;">Windows</li>
    <li class="service" style="left:487px; top:112px;">Plumbing</li>
    <li class="service" style="left:101px; top:143px;">Painting</li>
    <li class="service" style="left:293px; top:143px;">Walls &amp; Fences</li>
    <li class="service" style="left:487px; top:143px;">Gardening</li>
  </ul>

  <p class="tagline">
    Is it B<span class="wobble wobble--up">R</span><span class="wobble wobble--down">O</span><span class="wobble wobble--tilt">K</span><span class="wobble wobble--down">E</span><span class="wobble wobble--up">N</span>???<br>
    Not a problem
  </p>

  <p class="offer">Handyman<br>Services</p>

  <svg class="address-frame" width="1200" height="351" aria-hidden="true">
    <polyline points="853,111 654,111 654,219" fill="none" stroke="var(--ink)" stroke-width="2.5"/>
    <polyline points="1124,160 1124,269 926,269" fill="none" stroke="var(--ink)" stroke-width="2.5"/>
  </svg>
  <address class="address">
    42 Larkvale Hollow Road<br>
    Wrenford, Ct<br>
    06419
  </address>

  <footer class="footer">
    <svg class="footer-cut" width="1200" height="65" aria-hidden="true">
      <polygon points="327,0 364,0 322,65 285,65" fill="var(--paper)"/>
    </svg>
    <div class="owner-name">Dale P. Whitcombe</div>
    <div class="phone">
      <svg class="phone-icon" viewBox="0 0 26 28" aria-hidden="true">
        <path d="M6 2 L10 2 L12 8 L9 10 C10 14 12 17 15 19 L18 16 L24 18 L24 23 C24 25 22 26 20 26 C11 25 3 17 2 7 C2 4 3 2 6 2 Z" fill="var(--paper)"/>
        <path d="M17 3 A8 8 0 0 1 24 10" fill="none" stroke="var(--paper)" stroke-width="1.6"/>
        <path d="M16 7 A4 4 0 0 1 20 11" fill="none" stroke="var(--paper)" stroke-width="1.6"/>
      </svg>
      <span>860-555-0187</span>
    </div>
    <div class="email">dwhitcombe584@mailnest.example</div>
  </footer>

</div>
</body>
</html>
```